Supplement Label Design - Sports Nutrition

Design a sports nutrition/weight loss supplement label that stands out in a crowded space. Supplement bottle size is 200c and label size is 7" x 2.5" approximately. We're looking for a design that emphasizes the products name called VYK. Vyk is an abbreviation for Vigor, Yield & Kinetics. We want VYK to be the center/focus point of the bottle and have a memorable design to it.

Target Market(s)

Men & Women over 18

Industry/Entity Type

Supplement

Font styles to use
Sans Serif
Decorative

Requirements
Must have
• Emphasis on the product name VYK. Serious, Inspirational & Motivational feel to the design, typo & colors. Electrocution/lightning feel to the text. Right hand side of label is our formulation. Left hand side is dedicated to explaining the trifecta formulation idea.
Nice to have
• For example, we like the graphic design of "Drum" energy drinks because you can identify the bottle from a distance and is memorable. We think that less is more and we'd like the design/colors do most of the talking.
Should not have
• Cartroon/animated style.

```html
<!DOCTYPE html>
<html lang="en">
<head>
<meta charset="utf-8">
<title>VYK Sports Nutrition Label</title>
<link rel="stylesheet" href="https://fonts.googleapis.com/css2?family=Oswald:wght@500;700&display=swap">
<style>
  :root {
    --backdrop: #4e6f7c;
    --navy: #1c1a5c;
    --navy-deep: #120f3d;
    --magenta: #d02a9c;
    --electric-blue: #1f8fe0;
    --white: #ffffff;
    --band-text: #14123f;
  }
  html, body {
    margin: 0;
    padding: 0;
    width: 1200px;
    height: 900px;
    overflow: hidden;
    background: var(--backdrop);
  }
  .label {
    position: absolute;
    left: 100px;
    top: 150px;
    width: 1000px;
    height: 600px;
    background: var(--navy);
    overflow: hidden;
    font-family: "Oswald", sans-serif;
  }
  .label-art {
    position: absolute;
    inset: 0 0 140px 0;
    background:
      radial-gradient(ellipse 32% 55% at 22% 42%, rgba(208, 42, 156, 0.55), transparent 70%),
      radial-gradient(ellipse 30% 50% at 80% 52%, rgba(31, 143, 224, 0.5), transparent 70%),
      linear-gradient(180deg, var(--navy) 0%, var(--navy-deep) 100%);
  }
  .brand {
    position: absolute;
    top: 40px;
    left: 0;
    right: 0;
    text-align: center;
  }
  .brand-name {
    display: block;
    font-weight: 700;
    font-size: 250px;
    line-height: 1;
    letter-spacing: 6px;
    color: var(--white);
  }
  .product-lines {
    position: absolute;
    top: 330px;
    left: 0;
    right: 0;
    text-align: center;
    color: var(--white);
    font-weight: 500;
    font-size: 42px;
    line-height: 1.2;
    letter-spacing: 2px;
    text-transform: uppercase;
  }
  .product-lines p { margin: 0; }
  .stripe-thin {
    position: absolute;
    left: 0;
    right: 0;
    top: 466px;
    height: 8px;
    background: var(--white);
  }
  .count-band {
    position: absolute;
    left: 0;
    right: 0;
    top: 490px;
    height: 80px;
    background: var(--white);
    display: flex;
    align-items: center;
    justify-content: center;
  }
  .count-band span {
    font-weight: 700;
    font-size: 50px;
    letter-spacing: 3px;
    color: var(--band-text);
    text-transform: uppercase;
  }
</style>
</head>
<body>
  <section class="label">
    <div class="label-art" role="img" aria-label="Magenta and electric blue wave-line pattern glowing on a deep navy field"></div>
    <div class="brand">
      <span class="brand-name">VYK</span>
    </div>
    <div class="product-lines">
      <p>Sports Nutrition</p>
      <p>Weight Loss Supplement</p>
    </div>
    <div class="stripe-thin"></div>
    <div class="count-band"><span>200 Capsules</span></div>
  </section>
</body>
</html>
```